Business card design Needed for new logo / Construction business, home extensions and new builds

We need a business card design using our new logo files which i will attach to this project :)

We are a small construction business specialising in home extensions, new builds and property development. We are very ambitious and would appreciate professional and elegant designs for our new business card.

Very serious about using the services on Sketchwharf and recently acquired our new logo from here :)

Please get involved, i will feedback when i can as i am very busy but can respond daily, thanks

Target Market(s)

People that want to build onto their houses, new building developments or adding too their existing property

Industry/Entity Type

Construction

Contact Information for Business Card

Thornley Pike Construction, Wilbur Fenwick (Managing Director), Tel 07829456172, email - info@thornley-pike, www.thornley-pike.co.uk

Colors

Designer to choose colors to be used in the design.

Requirements
Must have
• I like a deep grey on the back please. A lot of you have provided black from and back, try mixing things up a little. The black looks cool 😎 Thanks

```html
<!DOCTYPE html>
<html lang="en">
<head>
<meta charset="utf-8">
<title>Thornley Pike Construction – Business Card</title>
<link rel="stylesheet" href="https://fonts.googleapis.com/css2?family=Montserrat:wght@400;600;700&display=swap">
<style>
  :root {
    --backdrop: #d9d9d9;
    --card-dark: #2f2f2f;
    --card-dark-edge: #262626;
    --gold-light: #e9c57a;
    --gold-mid: #c8963e;
    --gold-deep: #a8731f;
    --silver-light: #e4e6ea;
    --silver-deep: #9a9ea6;
    --ink: #111111;
    --text-light: #f2f2f2;
    --divider: #7a7a7a;
  }
  * { box-sizing: border-box; margin: 0; padding: 0; }
  html, body {
    width: 1200px; height: 768px; overflow: hidden;
    background: var(--backdrop);
    font-family: "Montserrat", sans-serif;
  }
  .canvas {
    width: 1200px; height: 768px;
    display: flex; align-items: center; justify-content: center; gap: 48px;
  }
  .card {
    position: relative;
    width: 532px; height: 304px;
    border-radius: 22px;
    overflow: hidden;
    box-shadow: 0 10px 28px rgba(0,0,0,0.25);
  }

  /* Back side – gold */
  .card--back {
    background: linear-gradient(120deg, var(--gold-mid) 0%, var(--gold-light) 45%, var(--gold-deep) 100%);
    display: flex; flex-direction: column; align-items: center; justify-content: center;
  }
  .back-brand {
    display: flex; align-items: center; gap: 12px;
    font-weight: 700; font-size: 30px; color: var(--ink);
    letter-spacing: 0.02em;
    margin-bottom: 58px;
  }
  .brand-square { width: 18px; height: 18px; background: var(--ink); }
  .back-web {
    position: absolute; bottom: 46px; width: 100%;
    text-align: center;
    font-size: 13px; letter-spacing: 0.32em; color: var(--ink);
  }

  /* Front side – deep grey */
  .card--front {
    background: linear-gradient(160deg, var(--card-dark) 0%, var(--card-dark-edge) 100%);
  }
  .front-swoosh { position: absolute; inset: 0; }
  .front-brand {
    position: absolute; left: 34px; top: 96px; width: 210px;
    text-align: center;
    color: var(--gold-mid);
    font-weight: 600; font-size: 19px; line-height: 1.3;
    letter-spacing: 0.06em; text-transform: uppercase;
  }
  .front-divider {
    position: absolute; left: 262px; top: 50px;
    width: 1px; height: 150px; background: var(--divider);
  }
  .front-details { position: absolute; left: 284px; top: 62px; }
  .person-name { font-weight: 700; font-size: 25px; color: var(--gold-mid); }
  .person-role { font-size: 15px; color: var(--text-light); margin-top: 2px; }
  .contact-list { list-style: none; margin-top: 18px; }
  .contact-item {
    display: flex; align-items: center; gap: 8px;
    font-size: 14px; color: var(--text-light); line-height: 1.55;
  }
  .contact-icon { width: 12px; height: 12px; flex: none; }
</style>
</head>
<body>
<main class="canvas">

  <section class="card card--back" aria-label="Card back">
    <div class="back-brand"><span class="brand-square"></span>Thornley Pike</div>
    <p class="back-web">www.thornley-pike.co.uk</p>
  </section>

  <section class="card card--front" aria-label="Card front">
    <svg class="front-swoosh" viewBox="0 0 532 304" preserveAspectRatio="none" aria-hidden="true">
      <defs>
        <linearGradient id="gold-band" x1="0" y1="0" x2="1" y2="0">
          <stop offset="0" stop-color="#b88130"/>
          <stop offset="0.4" stop-color="#ecc77c"/>
          <stop offset="1" stop-color="#b07a25"/>
        </linearGradient>
        <linearGradient id="silver-band" x1="0" y1="0" x2="1" y2="0">
          <stop offset="0" stop-color="#8d9198"/>
          <stop offset="0.6" stop-color="#e4e6ea"/>
          <stop offset="1" stop-color="#a6aab1"/>
        </linearGradient>
      </defs>
      <path d="M0,196 C110,238 300,252 532,254 L532,304 L0,304 Z" fill="url(#gold-band)"/>
      <path d="M0,190 C110,232 300,244 532,240 L532,256 C300,256 110,244 0,198 Z" fill="url(#silver-band)"/>
    </svg>

    <div class="front-brand">Thornley Pike<br>Construction</div>
    <div class="front-divider"></div>

    <div class="front-details">
      <h1 class="person-name">Wilbur Fenwick</h1>
      <p class="person-role">Managing Director</p>
      <ul class="contact-list">
        <li class="contact-item">
          <svg class="contact-icon" viewBox="0 0 24 24" aria-hidden="true"><path fill="#c8963e" d="M6.6 10.8a15 15 0 0 0 6.6 6.6l2.2-2.2c.3-.3.7-.4 1-.2 1.1.4 2.3.6 3.6.6.6 0 1 .4 1 1V20c0 .6-.4 1-1 1A17 17 0 0 1 3 4c0-.6.4-1 1-1h3.5c.6 0 1 .4 1 1 0 1.3.2 2.5.6 3.6.1.3 0 .7-.2 1z"/></svg>
          07829456172
        </li>
        <li class="contact-item">
          <svg class="contact-icon" viewBox="0 0 24 24" aria-hidden="true"><rect x="2" y="5" width="20" height="14" fill="#c8963e"/><path d="M2 5l10 8 10-8" fill="none" stroke="#2f2f2f" stroke-width="2"/></svg>
          info@thornley-pike
        </li>
        <li class="contact-item">
          <svg class="contact-icon" viewBox="0 0 24 24" aria-hidden="true"><circle cx="12" cy="12" r="10" fill="#c8963e"/><path d="M2 12h20M12 2c3 3 3 17 0 20M12 2c-3 3-3 17 0 20" fill="none" stroke="#2f2f2f" stroke-width="1.5"/></svg>
          www.thornley-pike.co.uk
        </li>
      </ul>
    </div>
  </section>

</main>
</body>
</html>
```